Business Card Design Project

Business card design with a funky, clean, modern design. Business is an immigration consultancy. Client base will be Canadian employers wanting to hire or retain foreign workers and foreign nationals wanting to immigrate to Canada.

Full color possible, but should incorporate red/white/black as per the logo to be provided. Double sided card design.

Target Market(s)

Canadian employers looking to hire/retain staff and also foreign nationals immigrating to Canada

Industry/Entity Type

Business

Requirements
Must have
• Logo (to be provided)
Name (Marla Voskuil, Immigration Consultant)
Phone (604) 731-5562
E-mail: marla@tallowbrookmigration.example
Web: www.tallowbrookmigration.example

Nice to have
• Tag Line
Clean, modern style

```html
<!DOCTYPE html>
<html lang="en">
<head>
<meta charset="utf-8">
<title>Tallowbrook Migration – Business Card</title>
<link href="https://fonts.googleapis.com/css2?family=PT+Serif:wght@400;700&display=swap" rel="stylesheet">
<style>
  :root {
    --page-bg: #d9d9d9;
    --brand-red: #d9141b;
    --brand-red-deep: #b70f15;
    --card-white: #f4f4f4;
    --card-white-shade: #e9e9e9;
    --ink: #141414;
    --ink-soft: #333333;
    --on-red: #ffffff;
  }
  * { box-sizing: border-box; margin: 0; padding: 0; }
  html, body {
    width: 1200px; height: 1200px; overflow: hidden;
    background: var(--page-bg);
    font-family: "PT Serif", Georgia, serif;
  }
  .canvas {
    position: relative; width: 1200px; height: 1200px;
  }
  .card {
    position: absolute; left: 180px; width: 840px; height: 480px;
    box-shadow: 0 10px 28px rgba(0,0,0,0.18);
    overflow: hidden;
  }
  /* Front side */
  .card--front { top: 90px; }
  .card-front__pattern {
    position: absolute; inset: 0;
    background: radial-gradient(ellipse at 50% 45%, var(--brand-red) 0%, var(--brand-red-deep) 100%);
  }
  .card-front__brand {
    position: absolute; left: 0; right: 0; top: 105px;
    display: flex; flex-direction: column; align-items: center;
  }
  .brand-dot {
    width: 120px; height: 120px; border-radius: 50%;
    border: 4px solid var(--on-red);
  }
  .card-front__name {
    margin-top: 34px;
    color: var(--on-red);
    font-weight: 700; font-size: 52px; letter-spacing: 2px;
    text-transform: uppercase; text-align: center; line-height: 1.05;
  }
  /* Back side */
  .card--back { top: 630px; }
  .card-back__pattern {
    position: absolute; inset: 0;
    background: linear-gradient(180deg, var(--card-white) 0%, var(--card-white-shade) 100%);
  }
  .card-back__mark {
    position: absolute; left: 392px; top: 38px; transform: translateX(-50%);
    width: 56px; height: 56px; border-radius: 50%;
    background: var(--brand-red);
  }
  .card-back__person {
    position: absolute; left: 60px; top: 150px; width: 310px;
    color: var(--ink);
  }
  .person__name { font-size: 34px; font-weight: 400; white-space: nowrap; }
  .person__title { font-size: 26px; text-align: right; padding-right: 6px; margin-top: 4px; color: var(--ink-soft); }
  .card-back__divider {
    position: absolute; left: 390px; top: 120px; width: 4px; height: 170px;
    background: linear-gradient(180deg, rgba(217,20,27,0) 0%, var(--brand-red) 50%, rgba(217,20,27,0) 100%);
  }
  .card-back__contacts {
    position: absolute; left: 412px; top: 150px;
    list-style: none; color: var(--ink);
    font-size: 19px; line-height: 1;
  }
  .contact { display: flex; align-items: center; gap: 10px; margin-bottom: 16px; white-space: nowrap; }
  .contact svg { width: 20px; height: 20px; flex: none; }
  .card-back__company {
    position: absolute; left: 60px; width: 320px; top: 335px;
    color: var(--ink); font-weight: 700; font-size: 30px;
    text-transform: uppercase; text-align: center; letter-spacing: 1px; line-height: 1.1;
  }
</style>
</head>
<body>
<main class="canvas">
  <section class="card card--front" aria-label="Card front">
    <div class="card-front__pattern" role="img" aria-label="Red background with faint repeating maple leaf pattern"></div>
    <div class="card-front__brand">
      <div class="brand-dot"></div>
      <p class="card-front__name">Tallowbrook<br>Migration</p>
    </div>
  </section>

  <section class="card card--back" aria-label="Card back">
    <div class="card-back__pattern" role="img" aria-label="White background with faint repeating maple leaf pattern"></div>
    <div class="card-back__mark"></div>
    <div class="card-back__person">
      <p class="person__name">Marla Voskuil</p>
      <p class="person__title">RCIC</p>
    </div>
    <div class="card-back__divider"></div>
    <ul class="card-back__contacts">
      <li class="contact">
        <svg viewBox="0 0 24 24" aria-hidden="true"><rect x="7" y="2" width="10" height="20" rx="2" fill="none" stroke="#d9141b" stroke-width="2"/><circle cx="12" cy="18" r="1.2" fill="#d9141b"/></svg>
        <span>(604) 731-5562</span>
      </li>
      <li class="contact">
        <svg viewBox="0 0 24 24" aria-hidden="true"><rect x="2" y="5" width="20" height="14" rx="1.5" fill="#d9141b"/><path d="M3 6l9 7 9-7" fill="none" stroke="#fff" stroke-width="1.6"/></svg>
        <span>marla@tallowbrookmigration.example</span>
      </li>
      <li class="contact">
        <svg viewBox="0 0 24 24" aria-hidden="true"><path d="M21 3L3 10l7 3 3 7z" fill="#d9141b"/></svg>
        <span>www.tallowbrookmigration.example</span>
      </li>
    </ul>
    <p class="card-back__company">Tallowbrook Migration</p>
  </section>
</main>
</body>
</html>
```